Flowy subpage design wanted for a modern tax/accounting firm in Switzerland

--- Introduction ---
We are a tax and accounting firm in Switzerland. We provide services for expats living in Switzerland, our service is quite exclusive and modern (digital).

We just relaunched our website www.fiscorana.ch and are happy with the design, so the desired subpage (more details below) should of course fit in.

--- Main brief ---
Please see Word File attached. The page has to include the whole text (11 chapters). A very intuitive, flowy design on only one subpage (not one page per chapter) is a MUST. Also, it is key that the design is supporting the content of the individual chapters, so it would be advantageous if you'd have a good unterstanding of the text attached.

--- Further information ---
A similar example would be this one: https://www2.brennick.com/ch/en/pages/tax/articles/living-working-switzerland.html

This one is similar in what concerns the content, but NOT what we are looking for designwise. It is very simple and looks "thrown together", just not aesthetically pleasing in our opinion.

--- Final thoughts ---
- If you blow our minds with your design, we will certainly have future work for you.
- Our clients are between 20-50 years old, well educated, high income / high wealth, English speaking and living in Switzerland.
- CI/CD information:
Fonts
Montserrat regular / medium italic / bold
Colors
White #ffffffff
Darkblue #0a2b46
Darkblue 25% #b5bfc8
Darkblue 50% #8595a4
Greenblue #0d4261

We are looking forward to your designs!
Updates

Thank you very much for the submitted designs and your efforts. Unfortunately, none of the designs meet our expectations so far. Please note the following: - Designs that do not take CI into account will not be looked at more closely. - We have received many simple designs with very simple structure and accordion elements. But more important than the simple structure is an eye-catching design! Make it flowy and beautiful - We don't want pictures of Swiss vehicles, passes or other pictures that don't actively support the text. If you can make an illustration that really fits the context, fine, otherwise better leave it without. Thank you

Target Market(s)

Expats living in Switzerland. High income earners / high net worth individuals

Industry/Entity Type

tax/accounting

Number of Pages Required

1 page

Font styles to use
Other font styles liked:
• Montserrat

Colors
0054AA
0677BA
7BADD7
CADEEF
E8F1F8

Requirements
Must have
• based on general website design
Nice to have
• intuitive, flowy, attractive representation of much text
Should not have
• basic copy/paste of the text in sections :)

```html
<!DOCTYPE html>
<html lang="en">
<head>
<meta charset="utf-8">
<title>Subpage component collection</title>
<link href="https://fonts.googleapis.com/css2?family=Montserrat:ital,wght@0,400;0,500;0,600;0,700;1,500&display=swap" rel="stylesheet">
<style>
:root{
  --page:#ececec;
  --white:#ffffff;
  --darkblue:#0a2b46;
  --greenblue:#0d4261;
  --db25:#b5bfc8;
  --db50:#8595a4;
  --blue:#0054aa;
  --mid:#0677ba;
  --sky:#7badd7;
  --ice:#cadeef;
  --frame:#a9adb1;
  --ink:#2b3138;
}
*{box-sizing:border-box;margin:0;padding:0}
html,body{width:816px;height:1200px;overflow:hidden}
body{background:var(--page);font-family:'Montserrat',sans-serif;color:var(--ink);position:relative}
.sheet-title{position:absolute;left:0;width:762px;top:40px;text-align:center;font-size:16.5px;font-weight:700;color:var(--greenblue)}
.section-label{position:absolute;font-size:11.5px;font-weight:600;color:var(--ink);white-space:nowrap}
.frame{position:absolute;border:1px solid var(--frame);border-radius:10px}

/* 1 - tiles */
.tile-grid{position:absolute;left:55px;top:206px;width:239px;height:163px;display:grid;grid-template-columns:repeat(4,1fr);grid-template-rows:repeat(4,1fr)}
.tile{position:relative;color:var(--white);font-size:5.3px;font-weight:700;line-height:1.15;display:flex;align-items:flex-end;padding:0 5px 5px 6px}
.tile.photo-mount{background:linear-gradient(160deg,#9aabbb,#4d6479)}
.tile.photo-town{background:linear-gradient(170deg,#7f95ad,#36495d)}
.tile.photo-lake{background:linear-gradient(120deg,#5d7a46,#2f6d77 60%,#6f8b98)}
.link-box{position:absolute;left:55px;top:417px;width:258px;height:65px;background:var(--greenblue);display:flex;gap:8px;padding:14px 10px 0 18px}
.link-box ul{list-style:disc;color:var(--sky);font-size:3.6px;line-height:7.6px}
.link-box li{margin-left:4px}
.link-box a{color:var(--sky)}

/* table of contents: set at double size and scaled to half */
.tree{position:absolute;left:337px;top:164px;width:152px;height:736px;overflow:hidden;transform:scale(.5);transform-origin:0 0;font-size:6.2px;font-weight:600;line-height:12.1px;color:var(--darkblue);list-style:none}
.tree ul{list-style:none;border-left:1.2px solid var(--darkblue);margin-left:1px;padding-left:14px}
.tree li{position:relative}
.tree .caret,.tree .side{padding-right:14px}
.tree .caret::after{content:"›";position:absolute;right:2px;top:0;transform:rotate(90deg)}
.tree .side::after{content:"‹";position:absolute;right:2px;top:0}

/* 3 - accordion */
.accordion-item{position:absolute;left:487px;width:258px;height:19px;background:var(--white);box-shadow:0 2px 4px rgba(0,0,0,.12);display:flex;align-items:center;justify-content:space-between;padding:0 10px;font-size:4.4px;font-weight:600;color:var(--darkblue)}

/* 2 - search */
.search{position:absolute;left:474px;top:487px;width:152px;height:14.5px;background:var(--white);box-shadow:0 2px 4px rgba(0,0,0,.12);display:flex;align-items:center}
.search span{flex:1;font-size:3px;color:#b0b6bc;padding-left:12px}
.search .go{width:26px;height:11px;margin-right:2px;background:var(--greenblue);display:flex;align-items:center;justify-content:center}

.symbol{position:absolute;width:8px;height:8px;border-radius:50%;background:var(--mid);display:flex;align-items:center;justify-content:center}
.to-top{position:absolute;left:706px;top:364px;width:19px;height:19px;background:#1565b8;display:flex;align-items:center;justify-content:center}

/* 5 - section titles */
.showcase{position:absolute;left:45px;top:676px;width:736px;height:475px;border:1px solid var(--frame);border-radius:10px}
.chapter{position:absolute;background:var(--greenblue);color:var(--white);font-size:7.8px;font-weight:700;line-height:9.4px;display:flex;flex-direction:column;justify-content:center;white-space:nowrap}
.chapter .num{display:block}
.pic{position:absolute}
</style>
</head>
<body>

<h1 class="sheet-title">This collection can use it sub page</h1>

<div class="section-label" style="left:31px;top:108px">1 - Ways to present page content</div>
<div class="section-label" style="left:459px;top:106px">3 &nbsp;- Accordions</div>
<div class="section-label" style="left:459px;top:292px">4 - Illustrative symbols</div>
<div class="section-label" style="left:649px;top:292px">6 - &nbsp;Back to top button</div>
<div class="section-label" style="left:459px;top:437px">2 - Search bar in page content</div>
<div class="section-label" style="left:45px;top:624px">5 - Section &nbsp;title with image</div>

<!-- 1 -->
<div class="frame" style="left:31px;top:148px;width:399px;height:409px"></div>
<div class="tile-grid">
  <div class="tile" style="background:#8c9196">Life in<br>Switzerland</div>
  <div class="tile" style="background:var(--sky);grid-row:span 2">Switzerland - a brief overview of the Alpine country</div>
  <div class="tile" style="background:#0b1020;grid-column:span 2;align-items:center;padding-top:20px">Immigrating to Switzerland -<br>These options are available</div>
  <div class="tile photo-mount" role="img" aria-label="Snowy mountain landscape">Indirect taxes in<br>Switzerland</div>
  <div class="tile photo-town" role="img" aria-label="Swiss old town with church spire">Other federal<br>taxes in<br>Switzerland</div>
  <div class="tile" style="background:var(--mid)">Rent and buy<br>in Switzerland</div>
  <div class="tile" style="background:var(--greenblue);grid-column:span 2;align-items:center;padding-top:4px">Double taxation agreements<br>between Switzerland and other<br>countries</div>
  <div class="tile" style="background:#0c3d5e;align-items:center;padding-top:14px">Childcare in<br>Switzerland</div>
  <div class="tile" style="background:var(--blue);grid-row:span 2">Labor Law in Switzerland - An Overview</div>
  <div class="tile" style="background:#4a5560">Public<br>transportation</div>
  <div class="tile photo-lake" role="img" aria-label="Alpine lake with a dog on the shore" style="grid-column:span 2">Recreation</div>
</div>

<div class="link-box">
  <ul style="width:78px">
    <li><a href="#">Life in Switzerland</a></li>
    <li><a href="#">Switzerland - a brief overview of the Alpine country</a></li>
    <li><a href="#">Immigrating to Switzerland - These options are available</a></li>
  </ul>
  <ul style="width:76px">
    <li><a href="#">Labor Law in Switzerland - An Overview</a></li>
    <li><a href="#">Double taxation agreements between Switzerland and other countries</a></li>
    <li><a href="#">Indirect taxes in Switzerland</a></li>
    <li><a href="#">Other federal taxes in Switzerland</a></li>
  </ul>
  <ul style="width:60px">
    <li><a href="#">Rent and buy in Switzerland</a></li>
    <li><a href="#">Childcare in Switzerland</a></li>
    <li><a href="#">Public transportation</a></li>
    <li><a href="#">Recreation</a></li>
  </ul>
</div>

<ul class="tree">
  <li class="caret">Life in Switzerland</li>
  <li><ul>
    <li class="caret">General</li>
    <li><ul>
      <li>4 official languages</li><li>Currency and banking</li><li>Public holidays</li>
      <li>Usual business and store opening hours</li><li>Electricity and water</li><li>Telephone and television</li>
    </ul></li>
    <li class="side">Living in Switzerland</li><li>The education system in Switzerland</li>
    <li>The healthcare system in Switzerland</li><li class="side">Driving in Switzerland</li>
    <li class="side">Public transport in Switzerland</li>
  </ul></li>
  <li class="caret">Switzerland - a brief overview of the Alpine country</li>
  <li><ul><li>A strong federation</li><li>A diverse population structure</li><li>Excellent economy</li><li>High standard of living</li><li>Exemplary pension system</li></ul></li>
  <li class="caret">Immigrating to Switzerland - These options are available</li>
  <li><ul><li>Immigrants with EU/EFTA citizenship</li><li>Immigrants from a third country</li><li class="side">Overview of the different work/establishment passes</li></ul></li>
  <li class="caret">Labor Law in Switzerland - An Overview</li>
  <li><ul><li>The employment contract</li><li>Probationary period</li><li>Termination of the employment relationship</li><li>When may the employer not terminate?</li></ul></li>
  <li class="caret">Double taxation agreements between Switzerland and other countries</li>
  <li><ul><li>Taxation of income and assets</li><li>Double taxation in the case of gifts or inheritances</li><li>Countries with which Switzerland has a double taxation agreement</li></ul></li>
  <li class="caret">Indirect taxes in Switzerland</li>
  <li><ul><li class="side">Value added tax</li><li class="side">Indirect taxes incurred when moving</li></ul></li>
  <li class="caret">Other federal taxes in Switzerland</li>
  <li><ul><li>Stamp duty</li><li>Withholding tax</li><li>EU Savings Directive</li></ul></li>
  <li class="caret">Rent and buy in Switzerland</li>
  <li><ul><li>Average prices</li><li>Renting is popular</li><li class="side">Rent property - what you need to consider</li><li class="side">Buying residential property - Paying attention to taxes</li></ul></li>
  <li class="caret">Childcare in Switzerland</li>
  <li><ul><li class="side">Different types of care</li><li class="side">Tax benefits for external childcare</li></ul></li>
  <li class="caret">Public transportation</li>
  <li><ul><li class="side">The public transport network</li></ul></li>
  <li class="caret">Recreation</li>
  <li><ul><li>Sports clubs</li><li>Volunteer</li><li>Integration courses</li><li>Mingle with the people</li></ul></li>
</ul>

<!-- 3 -->
<div class="frame" style="left:459px;top:148px;width:320px;height:108px"></div>
<div class="accordion-item" style="top:177px;align-items:flex-end;padding-bottom:1px;padding-left:13px">General
  <svg width="7" height="5" viewBox="0 0 7 5"><path d="M.5 1 3.5 4 6.5 1" fill="none" stroke="#0a2b46" stroke-width=".9"/></svg></div>
<div class="accordion-item" style="top:202px">Living in Switzerland
  <svg width="7" height="5" viewBox="0 0 7 5"><path d="M.5 1 3.5 4 6.5 1" fill="none" stroke="#0a2b46" stroke-width=".9"/></svg></div>

<!-- 4 -->
<div class="frame" style="left:459px;top:341px;width:115px;height:44px"></div>
<div class="symbol" style="left:490px;top:361px"><svg width="5" height="5" viewBox="0 0 5 5"><circle cx="2.5" cy="2.5" r="1.6" fill="none" stroke="#fff" stroke-width=".6"/></svg></div>
<div class="symbol" style="left:503px;top:361px"><svg width="5" height="5" viewBox="0 0 5 5"><path d="M1 4h3M1.5 3.5v-2h2v2M1 1.5 2.5.6 4 1.5" fill="none" stroke="#fff" stroke-width=".5"/></svg></div>
<div class="symbol" style="left:515px;top:361px"><svg width="5" height="5" viewBox="0 0 5 5"><path d="M.8 4h3.4M1 4V2.3h3V4M1 2.3 2.5 1 4 2.3" fill="none" stroke="#fff" stroke-width=".5"/></svg></div>
<div class="symbol" style="left:528px;top:361px"><svg width="5" height="5" viewBox="0 0 5 5"><rect x="1" y="1" width="3" height="3" fill="none" stroke="#fff" stroke-width=".5"/></svg></div>

<!-- 6 -->
<div class="frame" style="left:667px;top:339px;width:101px;height:70px"></div>
<div class="to-top"><svg width="10" height="7" viewBox="0 0 10 7"><path d="M1.5 5.5 5 2 8.5 5.5" fill="none" stroke="#fff" stroke-width="1.8"/></svg></div>

<!-- 2 -->
<div class="frame" style="left:457px;top:463px;width:192px;height:59px"></div>
<div class="search"><span>Search</span><div class="go"><svg width="5" height="5" viewBox="0 0 5 5"><circle cx="2.2" cy="2.2" r="1.4" fill="none" stroke="#fff" stroke-width=".5"/><path d="M3.2 3.2 4.3 4.3" stroke="#fff" stroke-width=".5"/></svg></div></div>

<!-- 5 -->
<div class="showcase">
  <div class="chapter" style="left:33px;top:22px;width:180px;height:59px;padding-left:13px"><span class="num">01</span>Life<br>in Switzerland</div>
  <div class="pic" role="img" aria-label="Old town bridge and church tower at dusk" style="left:152px;top:28px;width:87px;height:48px;background:linear-gradient(170deg,#5f7fa8,#a78c72 60%,#43505c)"></div>

  <div class="pic" role="img" aria-label="Alpine mountain range above green meadows" style="left:33px;top:105px;width:206px;height:81px;background:linear-gradient(180deg,#9aa7b4,#6f7a78 45%,#5d7f3a)"></div>
  <div class="chapter" style="left:74px;top:151px;width:128px;height:49px;padding-left:10px;overflow:visible"><span class="num">02</span>Switzerland - a brief<br>overview of the Alpine country</div>

  <div class="chapter" style="left:33px;top:231px;width:206px;height:63px;padding-left:13px"><span class="num">03</span>Immigrating<br>to Switzerland - These<br>options are available</div>
  <div class="pic" role="img" aria-label="Flag on a mountain viewpoint under clouds" style="left:164px;top:244px;width:55px;height:64px;background:linear-gradient(180deg,#d8dcdf,#9aa6ae 50%,#5f7a52)"></div>

  <div class="pic" role="img" aria-label="Hands typing on a laptop beside a contract" style="left:109px;top:343px;width:131px;height:84px;background:linear-gradient(135deg,#3d3a38,#8a7a66 55%,#c9a884)"></div>
  <div class="chapter" style="left:33px;top:357px;width:128px;height:56px;padding-left:13px"><span class="num">04</span>Labor Law<br>in Switzerland - An Overview</div>

  <div class="pic" role="img" aria-label="Business handshake" style="left:283px;top:108px;width:76px;height:38px;background:linear-gradient(90deg,#4a3e36,#b79a7c)"></div>
  <div class="chapter" style="left:322px;top:99px;width:167px;height:56px;padding-left:50px"><span class="num">05</span>Double taxation<br>agreements between<br>Switzerland and other countries</div>

  <div class="pic" role="img" aria-label="Calculator and financial charts on a desk" style="left:283px;top:179px;width:125px;height:72px;background:linear-gradient(135deg,#e4e6e9,#b7bec6 55%,#6b7f9c)"></div>
  <div class="chapter" style="left:381px;top:191px;width:108px;height:50px;padding-left:13px"><span class="num">06</span>Indirect<br>taxes in Switzerland</div>

  <div class="chapter" style="left:280px;top:287px;width:206px;height:56px;padding-left:13px"><span class="num">07</span>Other federal<br>taxes in Switzerland</div>
  <div class="pic" role="img" aria-label="Banknotes and calculator" style="left:391px;top:269px;width:79px;height:54px;background:linear-gradient(135deg,#d9c9b8,#eceae6 55%,#8a8d92)"></div>

  <div class="pic" role="img" aria-label="House model with keys on a plan" style="left:280px;top:373px;width:74px;height:46px;background:linear-gradient(135deg,#cfd4d8,#8a4a3a 55%,#b9bcc0)"></div>
  <div class="chapter" style="left:307px;top:367px;width:179px;height:60px;padding-left:66px"><span class="num">08</span>Rent and buy<br>in Switzerland</div>

  <div class="pic" role="img" aria-label="Children drawing at a table" style="left:528px;top:81px;width:188px;height:81px;background:linear-gradient(135deg,#9a7a5c,#c9a27a 50%,#d8c46a)"></div>
  <div class="chapter" style="left:558px;top:69px;width:128px;height:52px;padding-left:15px"><span class="num">09</span>Childcare<br>in Switzerland</div>

  <div class="pic" role="img" aria-label="Red train in a mountain valley" style="left:519px;top:210px;width:104px;height:74px;background:linear-gradient(180deg,#a9b7c6,#6f7f73 55%,#6a3a34)"></div>
  <div class="chapter" style="left:623px;top:210px;width:101px;height:74px;padding-left:12px;justify-content:flex-start;padding-top:13px"><span class="num">10</span>Public<br>transportation</div>

  <div class="chapter" style="left:527px;top:343px;width:206px;height:51px;padding-left:103px"><span class="num">11</span>Recreation</div>
  <div class="pic" role="img" aria-label="Skiers on a snowy slope" style="left:536px;top:308px;width:83px;height:76px;background:linear-gradient(180deg,#c8ccd2,#e4e6e8 55%,#8b8f96)"></div>
</div>

</body>
</html>
```